Business Card Design

I am a East Coast Florida based company specializing in hauling air conditioning units and Curb adaptors. I would like to see in the design a pickup truck hauling a goose neck trailer and the use of any colors.

Industry/Entity Type

Air Conditioning

Contact Information for Business Card

Pelican Ridge Freight email@ varela4163@mailbrook.com
Leonard (Lenny) Varela, Owner. hauling a/c units and curb adapters
Cell 772-555-0148

```html
<!DOCTYPE html>
<html lang="en">
<head>
<meta charset="utf-8">
<title>Pelican Ridge Freight – Business Card</title>
<link rel="stylesheet" href="https://fonts.googleapis.com/css2?family=Metamorphous&family=Old+Standard+TT:wght@400&family=Permanent+Marker&display=swap">
<style>
  :root {
    --red-top: #cf0000;
    --red-mid: #e0393b;
    --pink: #f2a3a3;
    --blush: #fbe3e3;
    --white: #ffffff;
    --silver-light: #f4f5f5;
    --silver: #cfd3d3;
    --silver-edge: #9da2a3;
    --ink: #111111;
    --accent: #d4141b;
  }
  html, body {
    margin: 0;
    padding: 0;
    overflow: hidden;
    background: #ffffff;
  }
  .card {
    position: relative;
    width: 1200px;
    height: 702px;
    overflow: hidden;
    background: linear-gradient(to bottom,
      var(--red-top) 0%,
      var(--red-mid) 30%,
      var(--pink) 55%,
      var(--blush) 80%,
      var(--white) 100%);
  }
  .company-name {
    position: absolute;
    left: 0;
    width: 1200px;
    top: 42px;
    margin: 0;
    text-align: center;
    font-family: "Metamorphous", serif;
    font-weight: 400;
    font-size: 78px;
    letter-spacing: 1px;
    color: var(--silver-light);
    text-shadow: 2px 3px 3px rgba(60, 0, 0, 0.55);
  }
  .banner {
    position: absolute;
    left: 0;
    top: 0;
    width: 1200px;
    height: 702px;
  }
  .vehicle-art {
    position: absolute;
    left: 238px;
    top: 202px;
    width: 442px;
    height: 172px;
    border-radius: 40px 60px 30px 30px;
    background: linear-gradient(to bottom, #2a2a2a, #0d0d0d);
  }
  .contact {
    position: absolute;
    margin: 0;
    font-family: "Old Standard TT", serif;
    font-size: 42px;
    color: var(--ink);
    line-height: 1;
    white-space: nowrap;
  }
  .owner-name { left: 61px; top: 466px; }
  .owner-title { left: 61px; top: 530px; }
  .email { left: 606px; top: 466px; font-size: 40px; }
  .phone { left: 610px; top: 530px; }
  .icon {
    position: absolute;
  }
  .icon-mail { left: 542px; top: 472px; width: 56px; height: 38px; }
  .icon-phone { left: 564px; top: 530px; width: 28px; height: 48px; }
  .tagline {
    position: absolute;
    left: 0;
    width: 1200px;
    top: 604px;
    margin: 0;
    text-align: center;
    font-family: "Permanent Marker", sans-serif;
    font-size: 30px;
    letter-spacing: 1px;
    color: var(--accent);
    transform: skewX(-8deg);
  }
</style>
</head>
<body>
  <main class="card">
    <h1 class="company-name">Pelican Ridge Freight</h1>

    <svg class="banner" viewBox="0 0 1085 620" preserveAspectRatio="none" aria-hidden="true">
      <defs>
        <linearGradient id="band-fill" x1="0" y1="0" x2="0" y2="1">
          <stop offset="0" stop-color="#e9ecec"/>
          <stop offset="0.5" stop-color="#cdd1d1"/>
          <stop offset="1" stop-color="#bfc4c4"/>
        </linearGradient>
      </defs>
      <path d="M0 200 L190 200 C240 200 250 155 320 155 L560 155 C630 155 640 210 700 210 C820 210 900 195 1040 200 Q1070 200 1070 215 L1070 305 Q1070 318 1050 318 C900 322 800 330 680 330 C630 330 620 385 560 385 L320 385 C250 385 240 340 190 337 L0 337 Z"
            fill="url(#band-fill)" stroke="#8f9495" stroke-width="4"/>
      <path d="M0 212 L192 212 C246 212 256 168 322 168 L558 168 C622 168 632 222 700 222 C820 222 900 208 1040 212 Q1058 212 1058 222 L1058 300 Q1058 306 1048 306 C900 310 800 318 680 318 C622 318 612 372 558 372 L322 372 C256 372 246 326 192 325 L0 325"
            fill="none" stroke="#ffffff" stroke-opacity="0.7" stroke-width="3"/>
    </svg>

    <div class="vehicle-art" role="img" aria-label="Black silhouette of a pickup truck, side view"></div>

    <p class="contact owner-name">Leonard Varela</p>
    <p class="contact owner-title">Owner</p>

    <svg class="icon icon-mail" viewBox="0 0 56 38" aria-hidden="true">
      <rect x="2" y="2" width="52" height="34" rx="3" fill="#ffffff" stroke="#111" stroke-width="3"/>
      <path d="M3 4 L28 22 L53 4" fill="none" stroke="#111" stroke-width="3"/>
      <path d="M3 34 L21 18 M53 34 L35 18" fill="none" stroke="#111" stroke-width="3"/>
    </svg>
    <p class="contact email">varela4163@mailbrook.com</p>

    <svg class="icon icon-phone" viewBox="0 0 28 48" aria-hidden="true">
      <rect x="2" y="2" width="24" height="44" rx="4" fill="#ffffff" stroke="#111" stroke-width="3"/>
      <rect x="5" y="7" width="18" height="30" fill="#111"/>
      <circle cx="14" cy="41" r="2" fill="#111"/>
    </svg>
    <p class="contact phone">772-555-0148</p>

    <p class="tagline">HAULING A/C UNITS AND CURB ADAPTERS</p>
  </main>
</body>
</html>
```